Marrowfen Vodka label redesign

This label was originally screen-printed. I would like it redesigned to fit a new rectangular paper label that will cover the screen-printed label of a different bottle than what was previously earmarked for a different product. I can easily resize the elements from the original label to fit the new size, but I would like to see some creative options for the new size. Show me what you've got!
Here are some guidelines:
New label must contain the butterfly and text "Marrowfen" in its existing font (that's our logo) the color is optional. It must also contain the barcode and all other text elements but font, style, size and color can change:
The Government warning text cannot be smaller. Style and font cannot change, but the justification can change.
The filigree does not have to stay.
The previous label was broken up into 3 panels. The new label will be one solid label encircling the bottle. The label size will be 10.5" x 5.5" (266.7 mm x 139.7 mm) AI template attached.

Target Market(s)

Women age 35 and up with disposable income

Font styles to use
Other font styles liked:
• Mostra Nuova

Colors

Designer to choose colors to be used in the design.

Requirements
Must have
• Class
Nice to have
• ArtDeco elements
Should not have
• Sharp edges

```html
<!DOCTYPE html>
<html lang="en">
<head>
<meta charset="utf-8">
<title>Marrowfen Vodka – Wraparound Label</title>
<link rel="stylesheet" href="https://fonts.googleapis.com/css2?family=Cherry+Swash&family=Cinzel:wght@700&family=Cinzel+Decorative:wght@700&family=Allura&family=Tinos:wght@400;700&display=swap">
<style>
  :root {
    --stage: #f4f4f4;
    --paper: #ebe8de;
    --aqua: #8fd0dc;
    --aqua-soft: #b7e2ea;
    --navy: #2e2b5c;
    --ink: #2f2f2f;
    --script-ink: #8d8a82;
  }
  html, body {
    margin: 0;
    width: 1200px;
    height: 1000px;
    overflow: hidden;
    background: var(--stage);
  }
  .label {
    position: absolute;
    left: 50px;
    top: 212px;
    width: 1100px;
    height: 576px;
    background: var(--paper);
    border-radius: 18px;
    display: flex;
    overflow: hidden;
    box-shadow: 0 6px 24px rgba(0,0,0,0.08);
  }
  .filigree-column {
    width: 180px;
    padding: 40px 22px;
    box-sizing: border-box;
    display: flex;
    flex-direction: column;
    justify-content: space-between;
  }
  .filigree {
    border-radius: 40px;
    background: radial-gradient(circle at 50% 45%, var(--aqua) 0%, var(--aqua-soft) 75%);
  }
  .filigree-column .filigree { height: 220px; }

  .back-panel {
    width: 300px;
    padding: 44px 24px 30px;
    box-sizing: border-box;
    font-family: "Tinos", serif;
    color: var(--ink);
    font-size: 10.5px;
    line-height: 1.34;
    display: flex;
    flex-direction: column;
  }
  .back-panel p { margin: 0 0 10px; }
  .distiller-info { font-weight: 700; }
  .back-footer {
    margin-top: auto;
    display: flex;
    justify-content: space-between;
    align-items: flex-end;
  }
  .tagline { font-family: "Cherry Swash", serif; font-size: 13px; margin-bottom: 4px; }
  .web { font-size: 10px; }
  .volume { font-family: "Cinzel", serif; font-size: 13px; }
  .symbols { display: flex; gap: 4px; margin-top: 6px; }

  .front-panel {
    position: relative;
    width: 440px;
    text-align: center;
    color: var(--navy);
  }
  .corner {
    position: absolute;
    width: 92px;
    height: 120px;
  }
  .corner.tl { left: -24px; top: 24px; border-radius: 0 40px 40px 0; }
  .corner.tr { right: -24px; top: 24px; border-radius: 40px 0 0 40px; }
  .corner.bl { left: -24px; top: 380px; border-radius: 0 40px 40px 0; }
  .corner.br { right: -24px; top: 380px; border-radius: 40px 0 0 40px; }

  .brand {
    margin-top: 64px;
    display: inline-flex;
    align-items: center;
    gap: 10px;
    font-family: "Cherry Swash", serif;
    font-size: 44px;
    color: var(--aqua);
  }
  .brand-dot {
    width: 14px; height: 14px;
    border-radius: 50%;
    background: var(--navy);
  }
  .product {
    margin: 28px 0 0;
    font-family: "Cinzel Decorative", serif;
    font-size: 88px;
    letter-spacing: 2px;
    line-height: 1;
  }
  .small-batch {
    margin-top: 36px;
    font-family: "Allura", cursive;
    font-size: 40px;
    color: var(--script-ink);
    line-height: 1;
  }
  .grade {
    font-family: "Cinzel", serif;
    font-size: 24px;
    margin-top: 2px;
  }
  .origin {
    margin: 14px auto 0;
    width: 260px;
    font-family: "Allura", cursive;
    font-size: 17px;
    line-height: 1.15;
    color: var(--script-ink);
  }
  .front-volume {
    position: absolute;
    right: 86px;
    bottom: 76px;
    font-family: "Cinzel", serif;
    font-size: 14px;
    color: var(--ink);
  }
</style>
</head>
<body>
<main class="label">
  <section class="filigree-column">
    <div class="filigree" role="img" aria-label="Aqua filigree ornament"></div>
    <div class="filigree" role="img" aria-label="Aqua filigree ornament"></div>
  </section>

  <section class="back-panel">
    <p>Marrowfen Spirits is an Oregon grown company located in the heart of the Willamette Valley with the goal of providing small-batch, hand-crafted, artisan spirits using as many locally sourced products as possible. Our mascot, the butterfly, is Oregon's state insect. For as it emerges it is light and like the butterfly, through much effort our vodka became something beautiful. We produce our vodka in small batches and it's blended with pristine McKenzie River water that has been filtered through the Northwest's unique volcanic geology, and our own process as well. The finished product has been filtered over 120 times through activated carbon for an incredibly clean, smooth finish.</p>
    <p>GOVERNMENT WARNING: (1) According to the Surgeon General, women should not drink alcoholic beverages during pregnancy because of the risk of birth defects. (2) Consumption of alcoholic beverages impairs your ability to drive a car or operate machinery, and may cause health problems.</p>
    <p class="distiller-info">Neutral Grain Spirits distilled 6x from corn.<br>Processed and bottled by hand<br>By Marrowfen Spirits llc<br>Fernhollow, OR</p>
    <div class="back-footer">
      <div>
        <div class="tagline">Savor Sensibly</div>
        <div class="web">marrowfenspirits.com</div>
      </div>
    </div>
    <div class="back-footer">
      <div class="volume">750ML</div>
      <svg class="symbols" width="110" height="14" viewBox="0 0 110 14" aria-hidden="true">
        <g fill="none" stroke="#2f2f2f" stroke-width="1.2">
          <circle cx="7" cy="7" r="6"/><circle cx="24" cy="7" r="6"/><circle cx="41" cy="7" r="6"/>
          <circle cx="58" cy="7" r="6"/><circle cx="75" cy="7" r="6"/><circle cx="92" cy="7" r="6"/>
        </g>
      </svg>
    </div>
  </section>

  <section class="front-panel">
    <div class="corner tl filigree" role="img" aria-label="Aqua filigree ornament"></div>
    <div class="corner tr filigree" role="img" aria-label="Aqua filigree ornament"></div>
    <div class="corner bl filigree" role="img" aria-label="Aqua filigree ornament"></div>
    <div class="corner br filigree" role="img" aria-label="Aqua filigree ornament"></div>

    <div class="brand"><span class="brand-dot"></span>Marrowfen</div>
    <h1 class="product">VODKA</h1>
    <div class="small-batch">Small-batch</div>
    <div class="grade">PREMIUM</div>
    <div class="origin">Alcohol 40% by volume 80 Proof<br>made in Willamette<br>Valley · Oregon · USA</div>
    <div class="front-volume">750ML</div>
  </section>

  <section class="filigree-column">
    <div class="filigree" role="img" aria-label="Aqua filigree ornament"></div>
    <div class="filigree" role="img" aria-label="Aqua filigree ornament"></div>
  </section>
</main>
</body>
</html>
```